Marrowin Brook Salon jojoba oil

Hello there!
I am looking to have a label created for a jojoba oil product I am launching. I have attached the logo of my company below. The label should have the following information on it as well:
Ingredients: pure jojoba oil
Size of the bottle: 118ml
And there might be more but I am working on this and will keep you posted.

```html
<!DOCTYPE html>
<html lang="en">
<head>
<meta charset="UTF-8">
<title>Marrowin Brook Salon – Jojoba Oil Label</title>
<link rel="stylesheet" href="https://fonts.googleapis.com/css2?family=Bebas+Neue&family=Raleway:wght@400;500&display=swap">
<style>
  :root {
    --backdrop: #f5e3d7;
    --band-light: #e8935a;
    --band-mid: #d9773d;
    --band-dark: #b95d2a;
    --panel: #252224;
    --panel-edge: #1c1a1b;
    --ink-light: #f2f0ee;
    --accent: #d9884f;
    --drip-tone: rgba(201, 138, 92, 0.22);
    --brand-ink: #2a2220;
  }
  * { box-sizing: border-box; margin: 0; padding: 0; }
  html, body {
    width: 1200px; height: 900px; overflow: hidden;
    background: var(--backdrop);
  }
  .canvas { position: relative; width: 1200px; height: 900px; }
  .label {
    position: absolute; left: 320px; top: 60px;
    width: 560px; height: 780px;
    box-shadow: 0 10px 30px rgba(90, 50, 25, 0.18);
  }
  .brand-band {
    position: absolute; left: 0; top: 0; width: 100%; height: 172px;
    background: linear-gradient(90deg, var(--band-dark) 0%, var(--band-mid) 18%, var(--band-light) 50%, var(--band-mid) 82%, var(--band-dark) 100%);
    display: flex; align-items: center; justify-content: center;
  }
  .brand-name {
    font-family: "Raleway", sans-serif; font-weight: 500;
    font-size: 34px; letter-spacing: 2px; color: var(--brand-ink);
    margin-top: 10px;
  }
  .product-panel {
    position: absolute; left: 0; top: 172px; width: 100%; height: 608px;
    background: linear-gradient(90deg, var(--panel-edge) 0%, var(--panel) 30%, var(--panel) 70%, var(--panel-edge) 100%);
  }
  .drip-art {
    position: absolute; left: 44px; top: 0; width: 70px; height: 570px;
    background: linear-gradient(180deg, var(--drip-tone) 0%, rgba(201, 138, 92, 0.08) 60%, var(--drip-tone) 100%);
  }
  .claim {
    position: absolute; left: 125px; top: 46px;
    font-family: "Raleway", sans-serif; font-size: 26px; font-weight: 400;
    color: var(--ink-light); letter-spacing: 0.5px;
  }
  .product-title {
    position: absolute; left: 120px; top: 82px;
    font-family: "Bebas Neue", sans-serif; font-weight: 400;
    color: var(--ink-light); line-height: 0.82;
  }
  .product-title .word-main { display: block; font-size: 158px; letter-spacing: -1px; }
  .product-title .word-sub { display: block; font-size: 118px; }
  .jojoba-art {
    position: absolute; left: 232px; top: 186px; width: 210px; height: 176px;
    border-radius: 50%;
    background: radial-gradient(ellipse at 50% 55%, #b5532a 0%, #8a3a1e 45%, #3f6b2a 75%, rgba(37,34,36,0) 100%);
  }
  .descriptor {
    position: absolute; left: 120px;
    font-family: "Raleway", sans-serif; font-weight: 400;
    font-size: 20px; color: var(--accent); letter-spacing: 0.3px;
  }
  .descriptor.pure { top: 392px; }
  .descriptor.benefit { top: 478px; }
  .process {
    position: absolute; left: 120px; top: 412px;
    font-family: "Bebas Neue", sans-serif; font-size: 66px;
    color: var(--ink-light); line-height: 1;
  }
  .volume {
    position: absolute; left: 165px; top: 524px;
    padding: 2px 8px;
    background: var(--ink-light); color: var(--panel);
    font-family: "Bebas Neue", sans-serif; font-size: 22px; line-height: 1.1;
    letter-spacing: 0.5px;
  }
</style>
</head>
<body>
<div class="canvas">
  <section class="label">
    <header class="brand-band">
      <span class="brand-name">Marrowin Brook Salon</span>
    </header>

    <div class="product-panel">
      <div class="drip-art" role="img" aria-label="Oil drip running down the label into a droplet with ripples"></div>

      <p class="claim">100% ORGANIC</p>
      <h1 class="product-title">
        <span class="word-main">JOJOBA</span>
        <span class="word-sub">OIL</span>
      </h1>
      <div class="jojoba-art" role="img" aria-label="Cluster of jojoba seeds with green leaves"></div>

      <p class="descriptor pure">PURE AND UNREFINED</p>
      <p class="process">COLD PRESSED OIL</p>
      <p class="descriptor benefit">SKIN NOURISHMENT</p>

      <span class="volume">4 FL OZ. 118 ML</span>
    </div>
  </section>
</div>
</body>
</html>
```